Wordpress theme for "plinkovault.net"

I am starting a Sports Blog called "Tallying @ Porch". I need a WordPress theme for the blog. I envisioned a theme with different sports score cards in the background (baseball, football, basketball, bowling, golf, cricket, etc.).
I know what I want, but it is hard to describe. I obviously want a professional looking blog (who doesn't) that is easy to navigate.
I like to have fun and be funny, and while I will post serious subjects, I want people to know I don't take myself too seriously.
Updates
I am afraid I may not have been entirely clear on the project, and I apologize. The blog is going to be about sports and social commentary. As far as the layout is concerned, I would like a three column layout with links to other blogs on one side and archives on the other. Also, I have found PICTURES of different types of scorecards on the internet, and I would like those images to be the BACKGROUND for the site, if possible.

```html
<!DOCTYPE html>
<html lang="en">
<head>
<meta charset="utf-8">
<title>Tallying @ Porch</title>
<link href="https://fonts.googleapis.com/css2?family=Open+Sans:wght@300;400;600;700&family=Oswald:wght@400;500;600&family=Montserrat:wght@300;400;700&family=Cinzel:wght@700&family=Arimo:wght@400&display=swap" rel="stylesheet">
<style>
:root{
  --green:#2f6b1f;
  --green-bright:#19b319;
  --red:#e41616;
  --ink:#222;
  --grey-bg:#ececec;
  --grey-tab:#cfcfcf;
  --dark-tab:#464646;
  --footer:#262626;
  --footer-bar:#2c2c2c;
  --muted:#8d8d8d;
  --link:#1b4fb5;
  --orange:#ee5a1c;
  --yellow:#f3e61a;
}
*{box-sizing:border-box;margin:0;padding:0}
html,body{width:977px;height:1200px;overflow:hidden;background:#fff;font-family:"Open Sans",sans-serif;color:var(--ink)}
.page{position:relative;width:977px;height:1200px}
.abs{position:absolute}

/* header */
.brand-dot{left:31px;top:66px;width:16px;height:16px;border-radius:50%;background:var(--green)}
.brand-name{left:56px;top:58px;font-family:"Open Sans",sans-serif;font-weight:600;font-size:26px;line-height:32px;color:var(--green);white-space:nowrap}
.search-btn{left:760px;top:40px;width:132px;height:18px;background:#111;color:#fff;font-family:"Oswald",sans-serif;font-size:8px;letter-spacing:.3px;text-align:center;line-height:18px}
.nav a{position:absolute;top:88px;font-size:14px;color:#222;text-decoration:none;font-weight:400;line-height:25px}
.nav .active{left:390px;width:66px;height:25px;background:var(--green);color:#fff;text-align:center}

/* hero */
.hero{left:0;top:125px;width:977px;height:326px;background:radial-gradient(ellipse at 50% 40%,#3d5a2c 0%,#22361a 60%,#15230f 100%)}
.hero-title{left:86px;top:144px;font-family:"Montserrat",sans-serif;font-weight:300;font-size:27px;letter-spacing:1.5px;color:#fff}
.back-icon{left:28px;top:150px}
.board{left:92px;top:203px;width:362px;height:115px;background:#000;border:3px solid #ddd;border-radius:3px}
.board .clock{position:absolute;left:98px;top:6px;width:166px;height:35px;border:2px solid #555}
.board .clock:after{content:":";position:absolute;left:76px;top:0;color:#fff;font-weight:700;font-size:22px}
.score{position:absolute;top:46px;width:80px;height:36px;background:#111;font-family:"Oswald",sans-serif;font-size:32px;line-height:36px;font-weight:600;text-align:center}
.score.home{left:14px;color:var(--green-bright)}
.score.away{right:14px;color:var(--red)}
.team{position:absolute;top:85px;color:#ddd;font-size:10px;font-family:"Montserrat",sans-serif}
.win-line{left:92px;top:326px;font-family:"Cinzel",serif;font-size:22px;font-weight:700;color:var(--yellow);letter-spacing:1px}
.panel-label{height:15px;width:165px;background:#c9c9c9;color:#666;font-size:9px;font-family:"Montserrat",sans-serif;padding-left:8px;line-height:15px}
.sbtn{position:absolute;height:28px;color:#fff;font-family:"Montserrat",sans-serif;font-size:6.5px;font-weight:700;text-align:center;line-height:26px;border:1px solid #eee}
.sbtn.g{background:var(--green-bright)}
.sbtn.r{background:var(--red)}
.outline-btn{width:89px;height:52px;border:2px solid #ddd;color:#fff;font-family:"Montserrat",sans-serif;font-size:8px;text-align:center;line-height:48px}

/* content */
.content{left:0;top:451px;width:977px;height:389px;background:var(--grey-bg)}
.col-head{height:37px;line-height:37px;font-size:14px;font-weight:400}
.other-head{left:0;top:461px;width:196px;background:var(--grey-tab);color:var(--green);padding-left:10px;font-weight:300}
.thumb{position:absolute;width:38px;height:38px;background:linear-gradient(135deg,#6b5a78,#2a3a66)}
.side-item{position:absolute;font-family:"Arimo",sans-serif;font-size:9.5px;color:#444;line-height:14px;white-space:nowrap}
.side-item a{color:var(--link);text-decoration:none;font-size:10px}
.side-item .meta{color:#aaa;font-size:7.5px;text-transform:uppercase}
.hot-head{left:201px;top:467px;font-family:"Oswald",sans-serif;font-weight:500;font-size:19px;color:var(--red);letter-spacing:-.3px;line-height:26px}
.hot-rule{left:290px;top:473px;width:486px;height:14px;background:#cfcfcf}
.story-img{position:absolute;left:198px;width:112px;height:76px}
.story-title{position:absolute;left:317px;font-family:"Oswald",sans-serif;font-size:19px;font-weight:500;color:var(--green);letter-spacing:-.3px}
.story-text{position:absolute;left:317px;width:478px;font-family:"Arimo",sans-serif;font-size:10.5px;line-height:11.5px;color:#111}
.story-text a{color:var(--green);text-decoration:none}
.tab-recent{left:783px;top:458px;width:96px;background:var(--grey-tab);color:var(--green);text-align:center}
.tab-most{left:879px;top:458px;width:98px;background:var(--dark-tab);color:#fff;text-align:center}

/* footer */
.footer{left:0;top:840px;width:977px;height:312px;background:var(--footer)}
.footer-bar{left:0;top:1152px;width:977px;height:48px;background:var(--footer-bar)}
.f-head{position:absolute;top:885px;font-family:"Montserrat",sans-serif;font-weight:700;font-size:10px;color:#fff;letter-spacing:.2px}
.about-head{left:16px;top:882px;font-family:"Oswald",sans-serif;font-size:14px;color:#fff;background:linear-gradient(90deg,#2f4a22,transparent);padding:0 6px;line-height:18px}
.f-text{position:absolute;font-size:11px;line-height:17px;color:#a9a9a9}
.post-img{position:absolute;left:263px;width:52px;height:50px}
.post-title{position:absolute;left:328px;font-family:"Montserrat",sans-serif;font-weight:700;font-size:11px;color:#ddd}
.post-date{position:absolute;left:328px;font-family:"Montserrat",sans-serif;font-size:7.5px;color:#777;letter-spacing:.5px}
.email{left:505px;top:970px;width:166px;height:27px;background:#2f2f2f;color:#666;font-size:9px;line-height:27px;padding-left:9px}
.join{left:671px;top:970px;width:45px;height:27px;background:var(--orange);color:#fff;font-family:"Montserrat",sans-serif;font-weight:700;font-size:8.5px;text-align:center;line-height:27px}
.contact-title{left:760px;top:925px;font-family:"Oswald",sans-serif;font-size:15px;color:#fff}
.social{position:absolute;top:1031px;width:29px;height:28px;border:1px solid #3a3a3a}
.copy{left:818px;top:1162px;font-family:"Oswald",sans-serif;font-size:7.5px;color:#bbb;letter-spacing:.2px}
</style>
</head>
<body>
<div class="page">

  <!-- header -->
  <div class="abs brand-dot"></div>
  <div class="abs brand-name">Tallying @ Porch</div>
  <div class="abs search-btn">SEARCH THE BLOG</div>
  <nav class="nav">
    <a class="active" href="#">Home</a>
    <a style="left:472px" href="#">Foot Ball<b>&gt;&gt;</b></a>
    <a style="left:560px" href="#">Cricket</a>
    <a style="left:628px" href="#">Basketball</a>
    <a style="left:719px" href="#">More Sports</a>
    <a style="left:828px" href="#">Contact Us</a>
  </nav>

  <!-- hero scorecard -->
  <div class="abs hero" role="img" aria-label="Close-up photo of green turf grass"></div>
  <svg class="abs back-icon" width="30" height="20" viewBox="0 0 30 20"><ellipse cx="15" cy="10" rx="13" ry="8" fill="none" stroke="#fff" stroke-width="2"/><path d="M21 10H10M14 6l-4 4 4 4" fill="none" stroke="#fff" stroke-width="2"/></svg>
  <div class="abs hero-title">Football Score Card</div>

  <div class="abs board">
    <div class="clock"></div>
    <div class="score home">12</div>
    <div class="score away">8</div>
    <div class="team" style="left:34px">Tigers</div>
    <div class="team" style="right:32px">Lions</div>
  </div>
  <div class="abs win-line">Tigers won the game.</div>

  <div class="abs panel-label" style="left:518px;top:202px">Tigers</div>
  <div class="sbtn g" style="left:520px;top:231px;width:81px">+Touchdown</div>
  <div class="sbtn g" style="left:610px;top:231px;width:31px">+1</div>
  <div class="sbtn g" style="left:650px;top:231px;width:31px">+2</div>
  <div class="sbtn g" style="left:520px;top:269px;width:81px">-Touchdown</div>
  <div class="sbtn g" style="left:610px;top:269px;width:31px">-1</div>
  <div class="sbtn g" style="left:650px;top:269px;width:31px">-2</div>
  <div class="sbtn g" style="left:520px;top:307px;width:81px">+Fieldgoal</div>
  <div class="sbtn g" style="left:606px;top:307px;width:75px">-Fieldgoal</div>

  <div class="abs panel-label" style="left:716px;top:202px">Lions</div>
  <div class="sbtn r" style="left:718px;top:231px;width:81px">+Touchdown</div>
  <div class="sbtn r" style="left:808px;top:231px;width:31px">+1</div>
  <div class="sbtn r" style="left:847px;top:231px;width:31px">+2</div>
  <div class="sbtn r" style="left:718px;top:269px;width:81px">-Touchdown</div>
  <div class="sbtn r" style="left:808px;top:269px;width:31px">-1</div>
  <div class="sbtn r" style="left:847px;top:269px;width:31px">-2</div>
  <div class="sbtn r" style="left:718px;top:307px;width:81px">+Fieldgoal</div>
  <div class="sbtn r" style="left:804px;top:307px;width:74px">-Fieldgoal</div>

  <div class="abs outline-btn" style="left:718px;top:377px">Game Over</div>
  <div class="abs outline-btn" style="left:840px;top:377px">New Game</div>

  <!-- content -->
  <div class="abs content" role="img" aria-label="Faded background photo of a baseball glove and scorecard"></div>

  <div class="abs col-head other-head">OTHER BLOGS TO READ</div>
  <div class="thumb" style="left:8px;top:506px" role="img" aria-label="Team celebrating with trophies"></div>
  <div class="side-item" style="left:54px;top:503px">14 Trophies for Harbor City<br><br><a href="#">postnook.com</a></div>
  <div class="thumb" style="left:8px;top:561px" role="img" aria-label="Football crowd celebration"></div>
  <div class="side-item" style="left:53px;top:558px">Millbrook United rocked NPL<br><br><a href="#" style="margin-left:8px">postnook.com</a></div>
  <div class="thumb" style="left:8px;top:616px" role="img" aria-label="Basketball player portrait"></div>
  <div class="side-item" style="left:53px;top:613px">Coming into focus<br><br><a href="#">postnook.com</a></div>
  <div class="thumb" style="left:8px;top:673px" role="img" aria-label="Basketball player in action"></div>
  <div class="side-item" style="left:53px;top:670px">Young Comets on the cusp of<br>comeback for the ages<br><a href="#">postnook.com</a></div>
  <div class="thumb" style="left:8px;top:731px" role="img" aria-label="Footballer in club shirt"></div>
  <div class="side-item" style="left:50px;top:728px">Dario Vell: I want to stay at<br>Harbor City<br><a href="#" style="margin-left:1px">postnook.com</a></div>

  <div class="abs hot-rule"></div>
  <div class="abs hot-head">HOT STORIES</div>

  <div class="story-img" style="top:505px;background:linear-gradient(160deg,#cfe3c6,#6fa044)" role="img" aria-label="Cricket bat and balls on grass"></div>
  <div class="story-title" style="top:504px">CRICKET NEWS</div>
  <div class="story-text" style="top:542px">Sed ut perspiciatis unde omnis iste natus error sit volupatetem accusantium doloremque lauantioum totam rem aperaim,eaque ab illo...... <a href="#">Read More</a></div>

  <div class="story-img" style="top:589px;background:linear-gradient(160deg,#8cae5a,#3f6b24)" role="img" aria-label="Player kicking a football"></div>
  <div class="story-title" style="top:588px">FOOTBALL NEWS</div>
  <div class="story-text" style="top:621px">Sed ut perspiciatis unde omnis iste natus error sit volupatetem accusantium doloremque lauantioum totam rem aperaim,eaque ab illo...... <a href="#">Read More</a></div>

  <div class="story-img" style="top:670px;background:linear-gradient(160deg,#7a4a24,#2e3f1c)" role="img" aria-label="Baseball in a leather glove"></div>
  <div class="story-title" style="top:669px">BASEBALL NEWS</div>
  <div class="story-text" style="top:705px">Sed ut perspiciatis unde omnis iste natus error sit volupatetem accusantium doloremque lauantioum totam rem aperaim,eaque ab illo...... <a href="#">Read More</a></div>

  <div class="story-img" style="top:752px;background:linear-gradient(160deg,#3d8a36,#1d4e1b)" role="img" aria-label="American football teams lined up on the field"></div>
  <div class="story-title" style="top:751px">AMERICAN FOOTBALL NEWS</div>
  <div class="story-text" style="top:790px">Sed ut perspiciatis unde omnis iste natus error sit volupatetem accusantium doloremque lauantioum totam rem aperaim,eaque ab illo...... <a href="#">Read More</a></div>

  <div class="abs col-head tab-recent">Recent</div>
  <div class="abs col-head tab-most">Most Read</div>
  <div class="thumb" style="left:800px;top:510px" role="img" aria-label="Football crowd celebration"></div>
  <div class="side-item" style="left:845px;top:507px">Millbrook United rocked NPL<br><span class="meta">No comments / by admin</span></div>
  <div class="thumb" style="left:801px;top:562px" role="img" aria-label="Team celebrating with trophies"></div>
  <div class="side-item" style="left:847px;top:559px">14 Trophies for Harbor City<br><span class="meta">2 comments / by admin</span></div>
  <div class="thumb" style="left:802px;top:614px" role="img" aria-label="Basketball player portrait"></div>
  <div class="side-item" style="left:848px;top:611px">Coming into focus<br><span class="meta">No comments / by admin</span></div>
  <div class="thumb" style="left:802px;top:673px" role="img" aria-label="Basketball player in action"></div>
  <div class="side-item" style="left:849px;top:670px;font-size:9px">Young Comets on the cusp of<br>comeback for the ages<br><span class="meta">No comments / by admin</span></div>
  <div class="thumb" style="left:800px;top:730px" role="img" aria-label="Footballer in club shirt"></div>
  <div class="side-item" style="left:846px;top:727px">Dario Vell: I want to stay at<br>Harbor City<br><span class="meta">No comments / by admin</span></div>

  <!-- footer -->
  <div class="abs footer"></div>
  <div class="abs about-head">ABOUT TALLYING @ PORCH</div>
  <div class="f-text" style="left:21px;top:918px;width:220px">Eros indoctum postulant pri id. Id mei legere ceteros. Vel essent facilisis id, everti iriure ius no.</div>
  <div class="f-text" style="left:21px;top:979px;width:220px">Verterem legendos at sit, perfecto appellantur ad vim.</div>

  <div class="f-head" style="left:263px">FROM OUR BLOG</div>
  <div class="post-img" style="top:920px;background:linear-gradient(135deg,#8a2a24,#3a1a18)" role="img" aria-label="Jersey number one"></div>
  <div class="post-title" style="top:922px">Heading for number one</div>
  <div class="post-date" style="top:943px">JULY 24TH, 2013</div>
  <div class="post-img" style="top:986px;background:linear-gradient(135deg,#e0a35a,#5a7aa8)" role="img" aria-label="Painted sprinter running"></div>
  <div class="post-title" style="top:988px">Running hard for the win!</div>
  <div class="post-date" style="top:1009px">JULY 17TH, 2013</div>
  <div class="post-img" style="top:1052px;background:linear-gradient(180deg,#3a4a6a,#6aa83a)" role="img" aria-label="Stadium pitch under lights"></div>
  <div class="post-title" style="top:1054px">Let the games begin</div>
  <div class="post-date" style="top:1075px">JULY 8TH, 2013</div>

  <div class="f-head" style="left:505px">NEWSLETTER SIGNUP</div>
  <div class="f-text" style="left:505px;top:918px;width:210px">Subscribe today and be the first one to receive the best sport news!</div>
  <div class="abs email">email address</div>
  <div class="abs join">JOIN</div>
  <div class="f-text" style="left:505px;top:1011px">We never spam!</div>

  <div class="f-head" style="left:746px">CONTACT INFORMATION</div>
  <div class="abs contact-title">YOUR CONTACT DETAILS</div>
  <div class="social" style="left:747px"></div>
  <div class="social" style="left:778px"></div>
  <div class="social" style="left:808px"></div>
  <div class="social" style="left:841px"></div>
  <div class="social" style="left:874px"></div>
  <div class="social" style="left:907px"></div>

  <div class="abs footer-bar"></div>
  <svg class="abs" style="left:800px;top:1163px" width="11" height="11" viewBox="0 0 11 11"><circle cx="5.5" cy="5.5" r="4.7" fill="none" stroke="#bbb"/></svg>
  <div class="abs copy">2013 TALLYING@PORCH. ALL RIGHTS RESERVED</div>

</div>
</body>
</html>
```